Strength Coach Business Card Design Project

I would like a business card design to complement my new logo. I would like the card to be clean, seek and strong!

Target Market(s)

Mostly adults and junior atheletes who are serious about changing their lives.

Industry/Entity Type

Business

Font styles to use
Serif

Colors

Designer to choose colors to be used in the design.

```html
<!DOCTYPE html>
<html lang="en">
<head>
<meta charset="utf-8">
<title>Summit Forge Fitness — Business Card</title>
<link href="https://fonts.googleapis.com/css2?family=Open+Sans:wght@400;700&display=swap" rel="stylesheet">
<style>
  :root {
    --backdrop: #1c1c1e;
    --card-white: #ececec;
    --card-edge: #f7f7f7;
    --brand-red: #a3161c;
    --deep-red: #5e0c12;
    --bright-red: #c91a20;
    --bar-grey: #dcdcdc;
    --ink: #2b2b2d;
  }
  * { box-sizing: border-box; margin: 0; padding: 0; }
  html, body {
    width: 1200px; height: 900px; overflow: hidden;
    background: var(--backdrop);
    font-family: "Open Sans", Arial, sans-serif;
  }
  .business-card {
    position: absolute; left: 150px; top: 190px;
    width: 900px; height: 520px;
    background: linear-gradient(135deg, var(--card-edge), var(--card-white) 60%);
    box-shadow: 0 18px 40px rgba(0,0,0,.55);
    overflow: hidden;
  }
  .accent-panel { position: absolute; inset: 0; width: 900px; height: 520px; }
  .contact-bar {
    position: absolute; height: 44px;
    background: var(--bar-grey);
    clip-path: polygon(18px 0, 100% 0, calc(100% - 18px) 100%, 0 100%);
    display: flex; align-items: center; gap: 18px;
    padding-left: 44px;
    color: var(--ink); font-size: 19px; letter-spacing: .3px;
  }
  .contact-bar svg { width: 20px; height: 20px; fill: var(--ink); flex: none; }
  .contact-address { left: 430px; top: 72px; width: 380px; }
  .contact-email   { left: 470px; top: 134px; width: 410px; }
  .contact-phone   { left: 510px; top: 196px; width: 340px; }
  .brand-lockup {
    position: absolute; left: 70px; top: 395px;
    display: flex; align-items: center; gap: 18px;
  }
  .brand-square { width: 44px; height: 44px; background: var(--brand-red); }
  .brand-name {
    font-weight: 700; font-size: 30px; line-height: 1.05;
    text-transform: uppercase; letter-spacing: 1px; color: var(--ink);
  }
</style>
</head>
<body>
  <div class="business-card">
    <svg class="accent-panel" viewBox="0 0 900 520" role="img" aria-label="Red low-poly geometric background texture">
      <defs>
        <linearGradient id="panelRed" x1="0" y1="0" x2="1" y2="1">
          <stop offset="0" stop-color="var(--deep-red)"/>
          <stop offset=".55" stop-color="var(--brand-red)"/>
          <stop offset=".8" stop-color="var(--bright-red)"/>
          <stop offset="1" stop-color="var(--deep-red)"/>
        </linearGradient>
      </defs>
      <polygon points="200,24 884,24 884,488 520,488" fill="url(#panelRed)"/>
    </svg>

    <div class="contact-bar contact-address">
      <svg viewBox="0 0 24 24"><path d="M12 2a7 7 0 0 0-7 7c0 5 7 13 7 13s7-8 7-13a7 7 0 0 0-7-7zm0 9.5A2.5 2.5 0 1 1 12 6.5a2.5 2.5 0 0 1 0 5z"/></svg>
      <span>27 Cedar Lane Tampa</span>
    </div>
    <div class="contact-bar contact-email">
      <svg viewBox="0 0 24 24"><path d="M3 5h18v14H3z M4 6.5v.6l8 5 8-5v-.6z" fill-rule="evenodd"/></svg>
      <span>hello@northpeakclub.com</span>
    </div>
    <div class="contact-bar contact-phone">
      <svg viewBox="0 0 24 24"><path d="M6.6 10.8a15 15 0 0 0 6.6 6.6l2.2-2.2a1 1 0 0 1 1-.25 11 11 0 0 0 3.6.6 1 1 0 0 1 1 1V20a1 1 0 0 1-1 1A17 17 0 0 1 3 4a1 1 0 0 1 1-1h3.5a1 1 0 0 1 1 1c0 1.25.2 2.45.6 3.6a1 1 0 0 1-.25 1z"/></svg>
      <span>555 018 2047</span>
    </div>

    <div class="brand-lockup">
      <div class="brand-square"></div>
      <div class="brand-name">Summit Forge<br>Fitness</div>
    </div>
  </div>
</body>
</html>
```